Business Card Design Project

Financial planning, Insurance and Real estate - Financial Services company

Contact Information for Business Card

Looking for something simple in design -
Brindlewood Capital LLC
Brindlewood Wealth Managment

```html
<!DOCTYPE html>
<html lang="en">
<head>
<meta charset="utf-8">
<title>Brindlewood Capital – Business Card</title>
<link href="https://fonts.googleapis.com/css2?family=Roboto+Condensed:wght@400;700&family=Roboto:wght@300;400&display=swap" rel="stylesheet">
<style>
  :root {
    --page: #ecebe8;
    --card: #f7f7f6;
    --brand-blue: #1b87c9;
    --band-grey: #b5b6b8;
    --ink: #4a4a4a;
    --ink-soft: #6b6b6b;
    --rule: #d6d6d6;
  }
  * { margin: 0; padding: 0; box-sizing: border-box; }
  html, body { width: 1200px; height: 911px; overflow: hidden; }
  body {
    background: var(--page);
    font-family: "Roboto Condensed", "Arial Narrow", sans-serif;
    color: var(--ink);
    position: relative;
  }
  .card {
    position: absolute;
    width: 560px;
    height: 320px;
    background: var(--card);
    box-shadow: 0 4px 14px rgba(0,0,0,0.12);
    overflow: hidden;
  }
  /* Front */
  .card--front { left: 60px; top: 100px; }
  .card--front .brand-panel {
    position: absolute; left: 0; top: 0; width: 290px; height: 302px;
    display: flex; flex-direction: column; align-items: center; justify-content: center; gap: 14px;
  }
  .brand-dot {
    width: 22px; height: 22px; border-radius: 50%; background: var(--brand-blue);
  }
  .brand-name {
    font-family: "Roboto Condensed", sans-serif;
    font-weight: 700; font-size: 20px; color: var(--brand-blue);
    letter-spacing: 0.2px;
  }
  .divider {
    position: absolute; left: 290px; top: 28px; width: 1px; height: 246px;
    background: var(--rule);
  }
  .contact-panel {
    position: absolute; left: 318px; top: 40px; width: 230px;
  }
  .person-name {
    font-size: 22px; font-weight: 400; color: var(--brand-blue);
    text-transform: uppercase; line-height: 1.1;
  }
  .person-title {
    font-size: 15px; text-transform: uppercase; color: var(--ink); margin-bottom: 6px;
  }
  .company, .address {
    font-size: 14px; color: var(--ink-soft); line-height: 1.35;
  }
  .contact-list { list-style: none; margin-top: 8px; }
  .contact-list li {
    display: flex; align-items: center; gap: 8px;
    font-family: "Roboto", sans-serif; font-weight: 300;
    font-size: 13.5px; color: var(--ink); line-height: 1.45;
  }
  .contact-list svg { width: 11px; height: 11px; flex: none; fill: var(--brand-blue); }
  .band {
    position: absolute; bottom: 0; height: 18px;
  }
  .band--blue { left: 0; width: 345px; background: var(--brand-blue); }
  .band--grey { left: 345px; right: 0; background: var(--band-grey); }

  /* Back */
  .card--back { left: 580px; top: 480px; }
  .back-url {
    position: absolute; left: 34px; top: 50%;
    transform: translate(-50%, -50%) rotate(90deg) translateY(-50%);
    transform-origin: center;
    font-family: "Roboto", sans-serif; font-weight: 400;
    font-size: 12px; letter-spacing: 6px; color: var(--ink);
    white-space: nowrap;
  }
  .back-brand {
    position: absolute; left: 0; right: 0; top: 0; bottom: 0;
    display: flex; align-items: center; justify-content: center; gap: 12px;
  }
</style>
</head>
<body>

<section class="card card--front" aria-label="Business card front">
  <div class="brand-panel">
    <span class="brand-dot"></span>
    <span class="brand-name">Brindlewood Wealth Managment</span>
  </div>
  <div class="divider"></div>
  <div class="contact-panel">
    <h1 class="person-name">Martin Hale</h1>
    <p class="person-title">CEO/Founder</p>
    <p class="company">Brindlewood Capital LLC</p>
    <p class="address">2140 Larkspur Road<br>Fairbanks, Alaska 99701</p>
    <ul class="contact-list">
      <li><svg viewBox="0 0 12 12"><path d="M2.5 0.5l2 2-1 1.5c.7 1.6 2 2.9 3.5 3.5l1.5-1 2 2-1.5 2C4.5 11.5.5 7.5.5 2z"/></svg>555 214 3870</li>
      <li><svg viewBox="0 0 12 12"><path d="M3 0h6a1 1 0 0 1 1 1v10a1 1 0 0 1-1 1H3a1 1 0 0 1-1-1V1a1 1 0 0 1 1-1zm0 1.5v8h6v-8z"/></svg>555 619 4207</li>
      <li><svg viewBox="0 0 12 12"><path d="M3 0h5v3H3zM1 4h10v6H9v2H3v-2H1zm3 5v2h4V9z"/></svg>555 730 1156</li>
      <li><svg viewBox="0 0 12 12"><path d="M0 2h12v8H0zm1 1l5 4 5-4v-.2H1z"/></svg>info@brindlewoodcap.com</li>
      <li><svg viewBox="0 0 12 12"><path d="M6 0a6 6 0 1 0 0 12A6 6 0 0 0 6 0zm0 1.2c.8.9 1.3 2.4 1.4 4.2H4.6C4.7 3.6 5.2 2.1 6 1.2zM4.6 6.6h2.8c-.1 1.8-.6 3.3-1.4 4.2-.8-.9-1.3-2.4-1.4-4.2z"/></svg>www.brindlewoodcap.com</li>
    </ul>
  </div>
  <div class="band band--blue"></div>
  <div class="band band--grey"></div>
</section>

<section class="card card--back" aria-label="Business card back">
  <p class="back-url">www.brindlewoodcap.com</p>
  <div class="back-brand">
    <span class="brand-dot"></span>
    <span class="brand-name">Brindlewood Capital LLC</span>
  </div>
</section>

</body>
</html>
```